Business card design needed

We are a Landscape business based in Sydney. We are targeting upper class clients that have the money to spend on their gardens.
We design, construct and maintain the gardens that we create.
We are looking for modern business card with our logo on it and the colours green grey\black/white scale. The design should communicate modern creative gardens. it should look classy and have a professional feel to it not cheap.should be two sides to the business card. Back side to have the words design construct maintain with possible the vine attached somewhere.
Updates

Project Deadline Extended
Reason: Hi Guys. Some of you have asked for a vector version of the vine so I just need some more time to find it as I don't have it here on my computer. Keep up the good work! Thanks Jon

Hi guys and girls.
You have all done a really good job so far. I have recently uploaded the vector for the vine and the logo as promissed. Looking forward to seeing you use them in your designs. Also i would like to see the words design-construct-maintain on the card as an option maybe on the back.
Thanks .

Target Market(s)

white collar, higher education, high social group in affluent areas

Industry/Entity Type

Business

Contact Information for Business Card

Bright Meadow Landscapes
Jonathan Perrow- 0431 592 740 Director( only need one name and number per card i.e. same design twice with different number and name.)
Paul tremaine- 0417 365 209 Director
www.bmlandscapes.example.au
ABN-872 310 954
Lic- 618094K

Requirements
Must have
• Logo which I am trying to upload but it is not working. I have contacted sketch forge to try and fix this.
Should not have
• Two s

```html
<!DOCTYPE html>
<html lang="en">
<head>
<meta charset="utf-8">
<title>Bright Meadow Landscapes – Business Cards</title>
<link rel="stylesheet" href="https://fonts.googleapis.com/css2?family=Josefin+Sans:wght@300;400;600&display=swap">
<style>
  :root {
    --bg-top: #e4e4e4;
    --bg-bottom: #c9c9c9;
    --card-dark: #2b2627;
    --ink: #231f20;
    --ink-soft: #4a4546;
    --leaf: #8cc63f;
    --paper: #ffffff;
    --rule: #9a9a9a;
  }
  * { box-sizing: border-box; margin: 0; padding: 0; }
  html, body { width: 1200px; height: 985px; overflow: hidden; }
  body {
    position: relative;
    background: linear-gradient(180deg, var(--bg-top), var(--bg-bottom));
    font-family: "Josefin Sans", Arial, sans-serif;
  }
  .card {
    position: absolute;
    width: 720px;
    height: 410px;
    border-radius: 22px;
    overflow: hidden;
    box-shadow: 0 14px 30px rgba(0,0,0,.28);
  }

  /* Back side */
  .card--back { left: 400px; top: 60px; background: var(--card-dark); color: var(--paper); }
  .vine-area {
    position: absolute; left: -60px; top: -40px; width: 460px; height: 360px;
    background: radial-gradient(closest-side at 50% 50%,
      rgba(140,198,63,.8) 0%,
      rgba(140,198,63,.45) 40%,
      rgba(255,255,255,.18) 70%,
      rgba(43,38,39,0) 100%);
  }
  .card--back .brand-name {
    position: absolute; right: 50px; top: 250px;
    font-size: 32px; font-weight: 600; letter-spacing: 1px; white-space: nowrap;
  }
  .card--back .web {
    position: absolute; right: 50px; top: 318px;
    font-size: 15px; letter-spacing: 4px; text-transform: uppercase; white-space: nowrap;
  }

  /* Front side */
  .card--front { left: 90px; top: 520px; background: var(--paper); color: var(--ink); }
  .swoosh { position: absolute; inset: 0; }
  .card--front .brand-name {
    position: absolute; left: 200px; top: 60px;
    font-size: 34px; font-weight: 600; letter-spacing: 1px; white-space: nowrap; color: var(--ink);
  }
  .person {
    position: absolute; right: 362px; top: 140px; text-align: right; white-space: nowrap;
  }
  .person__name { font-size: 18px; letter-spacing: 2px; text-transform: uppercase; color: var(--leaf); }
  .person__role { font-size: 15px; letter-spacing: 2px; text-transform: uppercase; color: var(--ink); margin-top: 6px; }
  .person__address { font-size: 12px; letter-spacing: 1.5px; text-transform: uppercase; color: var(--ink-soft); margin-top: 18px; }
  .divider { position: absolute; left: 372px; top: 135px; width: 1px; height: 135px; background: var(--rule); }
  .contacts { position: absolute; left: 388px; top: 140px; list-style: none; }
  .contacts li {
    display: flex; align-items: center; gap: 8px; white-space: nowrap;
    font-size: 14px; letter-spacing: 1.5px; color: var(--ink); margin-bottom: 7px;
  }
  .contacts svg { width: 17px; height: 17px; flex: none; }
</style>
</head>
<body>

<section class="card card--back" aria-label="Card back">
  <div class="vine-area" role="img" aria-label="Green and white flowing vine illustration"></div>
  <div class="brand-name">Bright Meadow Landscapes</div>
  <div class="web">www.brightmeadow.example.com</div>
</section>

<section class="card card--front" aria-label="Card front">
  <svg class="swoosh" viewBox="0 0 720 410" preserveAspectRatio="none" aria-hidden="true">
    <path d="M0,250 C150,275 320,335 470,410 L405,410 C290,352 140,302 0,285 Z" fill="var(--leaf)"/>
    <path d="M0,302 C140,322 280,368 365,410 L0,410 Z" fill="var(--ink)"/>
    <path d="M395,410 C500,395 610,368 720,330 L720,410 Z" fill="var(--leaf)"/>
    <path d="M440,410 C540,400 630,382 720,358 L720,410 Z" fill="var(--paper)"/>
  </svg>

  <div class="brand-name">Bright Meadow Landscapes</div>

  <div class="person">
    <div class="person__name">Paul Tremaine</div>
    <div class="person__role">Director</div>
    <div class="person__address">Suite # 118, Parkview Bldg, NSW 2065</div>
  </div>

  <div class="divider"></div>

  <ul class="contacts">
    <li>
      <svg viewBox="0 0 20 20"><circle cx="10" cy="10" r="10" fill="var(--leaf)"/><path d="M7 5l2 2-1 1.5c.8 1.6 1.9 2.7 3.5 3.5L13 11l2 2-1.5 2C9 14.5 5.5 11 5 6.5Z" fill="#fff"/></svg>
      0417-365-209
    </li>
    <li>
      <svg viewBox="0 0 20 20"><circle cx="10" cy="10" r="10" fill="var(--leaf)"/><rect x="7" y="4.5" width="6" height="11" rx="1" fill="#fff"/></svg>
      0452-718-306
    </li>
    <li>
      <svg viewBox="0 0 20 20"><circle cx="10" cy="10" r="10" fill="var(--leaf)"/><rect x="5" y="6" width="10" height="8" rx="1" fill="#fff"/><rect x="7" y="8" width="6" height="1.5" fill="var(--leaf)"/></svg>
      0468-203-915
    </li>
    <li>
      <svg viewBox="0 0 20 20"><circle cx="10" cy="10" r="10" fill="var(--leaf)"/><rect x="5" y="6.5" width="10" height="7" fill="#fff"/><path d="M5 6.5l5 4 5-4" stroke="var(--leaf)" stroke-width="1.2" fill="none"/></svg>
      name@bmlandscapes.example.au
    </li>
    <li>
      <svg viewBox="0 0 20 20"><circle cx="10" cy="10" r="10" fill="var(--leaf)"/><circle cx="10" cy="10" r="5" fill="none" stroke="#fff" stroke-width="1.3"/><path d="M5 10h10M10 5c-2 3-2 7 0 10M10 5c2 3 2 7 0 10" stroke="#fff" stroke-width="1" fill="none"/></svg>
      www.bmlandscapes.example.au
    </li>
  </ul>
</section>

</body>
</html>
```